White Rum brand needs bottle label

Looking for a label that will stand out on a shelf and feel like an instant classic. Corvane is a premium Caribbean blended white rum that was crafted as an escape from day-to-day stress and is all about making each day feel as though it's a vacation day. It was named after two local beaches and surf breaks both of which are party towns. I'd like the label to feel modern, sleek, and casual, while still feeling very slightly upscale and have a few subtle hints of it's tropical origin. Corvane should look suitable to drink in variety of situations such as a casual drink at the beach or a pool, a cocktail after a long day of work, or a night out at a bar or club. Please incorporate the logo somewhere in the label, whether that's just the mermaid or the entire design I'll leave that up to the designer. Whatever it is, it should have a look that is scalable and feels appropriate to consume in many settings while remembering it's Carribean and beach roots.

Target Market(s)

The target market is fairly broad. Target consumers are between 21-55, leaning slightly more towards the masculine crowd, full-time workers that enjoy drinking regularly.

Font styles to use
Serif
Sans Serif

Requirements
Must have
• Must have at least the mermaid part of the logo incorporated within the label.
Nice to have
• I'd like a bottle with a synthetic cork, that has a strap sealer over the top and a bottle shaped similar to Valdoro Tequila. Colors are designer's choice. Subtle floral or tropical notes (not too much) mixed into a fairly sleek and modern design.

```html
<!DOCTYPE html>
<html lang="en">
<head>
<meta charset="utf-8">
<title>Corvane White Rum Label</title>
<link rel="stylesheet" href="https://fonts.googleapis.com/css2?family=Kaushan+Script&display=swap">
<style>
  :root {
    --sea-deep: #16708f;
    --sea: #2188a7;
    --lagoon: #86b6a2;
    --sand: #f1c97c;
    --sunset: #f0a03e;
    --coral: #ef8064;
    --ember: #de5448;
    --wine: #6f2726;
    --ink: #0b0b0b;
    --foam: #ffffff;
  }
  html, body {
    margin: 0;
    padding: 0;
    width: 1200px;
    height: 2279px;
    overflow: hidden;
    background: #ffffff;
  }
  .label {
    display: block;
    width: 1200px;
    height: 2279px;
  }
  .brand-name {
    font-family: "Kaushan Script", cursive;
    font-size: 165px;
    fill: var(--foam);
  }
  .product-name {
    font-family: "Kaushan Script", cursive;
    font-size: 380px;
    fill: var(--ink);
  }
</style>
</head>
<body>
<svg class="label" viewBox="0 0 1200 2279" xmlns="http://www.w3.org/2000/svg">
  <defs>
    <linearGradient id="sky-to-sunset" x1="0" y1="0" x2="0" y2="1">
      <stop offset="0" style="stop-color:var(--sea-deep)"/>
      <stop offset="0.16" style="stop-color:var(--sea)"/>
      <stop offset="0.34" style="stop-color:var(--lagoon)"/>
      <stop offset="0.47" style="stop-color:var(--sand)"/>
      <stop offset="0.6" style="stop-color:var(--sunset)"/>
      <stop offset="0.7" style="stop-color:var(--coral)"/>
      <stop offset="0.83" style="stop-color:var(--ember)"/>
      <stop offset="0.9" style="stop-color:#b6403b"/>
      <stop offset="1" style="stop-color:var(--wine)"/>
    </linearGradient>
    <radialGradient id="frond-wash" cx="0.5" cy="0.42" r="0.62">
      <stop offset="0" stop-color="#ffffff" stop-opacity="0.55"/>
      <stop offset="0.55" stop-color="#ffffff" stop-opacity="0.38"/>
      <stop offset="1" stop-color="#ffffff" stop-opacity="0.12"/>
    </radialGradient>
  </defs>

  <rect class="label-ground" x="0" y="0" width="1200" height="2279" fill="url(#sky-to-sunset)"/>

  <rect class="palm-fronds" x="0" y="410" width="1200" height="1869" fill="url(#frond-wash)"
        role="img" aria-label="White palm frond silhouettes layered across the lower label"/>

  <g class="brand-lockup">
    <circle cx="600" cy="180" r="72" fill="none" stroke="#ffffff" stroke-width="6"/>
    <text class="brand-name" x="600" y="375" text-anchor="middle">Corvane</text>
  </g>

  <text class="product-name" transform="translate(790 1202) rotate(-90)" text-anchor="middle"
        textLength="1300" lengthAdjust="spacingAndGlyphs">WhiteRum</text>
</svg>
</body>
</html>
```